Design a BOLD Ad Design for Fitness Club

We are fitness facility that is about to run our new "Bright Parent Reboot" program and we need a bold design created for an ad that will run on Instagram and Facebook.

The ad needs to be eye catching, easy to read and attractive so that someone stops scrolling and clicks to join.

The add needs to be sized to 1080 x 1080, include our logo and the text "Bright Parent Reboot" and "Starting September 23rd"

I have included an example photo, which is to be used as an example only of a design style that stands out to us, (colors, female photo style, etc)

I have also included our logo, which the yellow color can be changed for this design.

Thank you and we look forward to seeing your design.

```html
<!DOCTYPE html>
<html lang="en">
<head>
<meta charset="utf-8">
<title>Bright Parent Reboot – Ad</title>
<link href="https://fonts.googleapis.com/css2?family=Bebas+Neue&family=Yellowtail&family=Montserrat:wght@400;600&display=swap" rel="stylesheet">
<style>
  :root {
    --page-bg: #a0a0a0;
    --ink: #050505;
    --white: #ffffff;
    --yellow: #f5cf0a;
    --gold: #e0b400;
    --grey-chevron: #3a3a3a;
    --dot: #d8d8d8;
  }
  html, body { margin: 0; padding: 0; }
  body {
    width: 1200px; height: 829px; overflow: hidden;
    background: var(--page-bg);
    position: relative;
  }
  .ad {
    position: absolute; left: 0; top: 0;
    width: 990px; height: 990px;
    background: var(--ink);
    overflow: hidden;
    transform: translate(303px, 118px) scale(0.6);
    transform-origin: 0 0;
    font-family: "Montserrat", sans-serif;
    color: var(--white);
  }
  .ad__photo { position: absolute; inset: 0; }
  .ad__dots { position: absolute; }
  .ad__dots--top { left: 432px; top: 24px; }
  .ad__dots--mid { left: 432px; top: 500px; }
  .title {
    position: absolute; left: 80px; top: 78px; margin: 0;
    font-family: "Bebas Neue", sans-serif; font-weight: 400;
    font-size: 132px; line-height: 1; letter-spacing: 1px;
    white-space: nowrap;
  }
  .title__script {
    position: absolute; left: 84px; top: 180px;
    font-family: "Yellowtail", cursive;
    font-size: 120px; line-height: 1; color: var(--yellow);
    white-space: nowrap;
  }
  .lead-arrows { position: absolute; left: -4px; top: 382px; }
  .start-label {
    position: absolute; left: 98px; top: 376px;
    font-size: 29px; letter-spacing: 8px; font-weight: 400;
  }
  .start-month {
    position: absolute; left: 80px; top: 428px; width: 240px; text-align: center;
    font-family: "Bebas Neue", sans-serif; font-size: 66px; line-height: 1;
    color: var(--yellow); letter-spacing: 1px;
  }
  .date-box {
    position: absolute; left: 82px; top: 498px; width: 234px; height: 260px;
    border: 2px solid var(--gold);
  }
  .date-box__day {
    position: absolute; left: 0; right: 0; top: 6px; text-align: center;
    font-family: "Bebas Neue", sans-serif; font-size: 270px; line-height: 1;
  }
  .date-box__year {
    position: absolute; left: 50%; bottom: -24px; transform: translateX(-50%);
    background: var(--ink); padding: 0 8px;
    font-size: 42px; letter-spacing: 10px; font-weight: 400; line-height: 1;
  }
  .back-chevrons { position: absolute; left: 380px; top: 708px; }
  .brand { position: absolute; left: 80px; top: 838px; width: 236px; text-align: center; }
  .brand__name {
    font-family: "Bebas Neue", sans-serif; font-size: 72px; line-height: 1;
    color: var(--yellow); letter-spacing: 1px;
  }
  .brand__tag {
    margin-top: 4px; font-size: 10px; font-weight: 600; letter-spacing: 1.5px;
    color: var(--yellow);
  }
  .follow {
    position: absolute; left: 724px; top: 884px;
    display: flex; align-items: center; gap: 10px;
    font-size: 15px; font-weight: 600; letter-spacing: 2px;
  }
  .follow__dot { width: 27px; height: 27px; border-radius: 50%; background: var(--white); }
</style>
</head>
<body>
  <section class="ad">
    <svg class="ad__photo" width="990" height="990" viewBox="0 0 990 990" role="img" aria-label="Athletic blonde woman in black sports top lifting a dumbbell in front of a yellow-lit gym">
      <defs>
        <linearGradient id="photoTone" x1="0" y1="0" x2="1" y2="1">
          <stop offset="0" stop-color="#1a1a1a"/>
          <stop offset="0.45" stop-color="#3a3126"/>
          <stop offset="0.75" stop-color="#b99200"/>
          <stop offset="1" stop-color="#f2c800"/>
        </linearGradient>
      </defs>
      <polygon points="600,0 990,0 990,990 320,990 480,820 600,640 640,320" fill="url(#photoTone)"/>
    </svg>

    <svg class="ad__dots ad__dots--top" width="110" height="40" viewBox="0 0 110 40">
      <g fill="var(--dot)"><circle cx="4" cy="4" r="2.5"/><circle cx="36" cy="4" r="2.5"/><circle cx="70" cy="4" r="2.5"/><circle cx="103" cy="4" r="2.5"/>
      <circle cx="4" cy="36" r="2.5"/><circle cx="36" cy="36" r="2.5"/><circle cx="70" cy="36" r="2.5"/><circle cx="103" cy="36" r="2.5"/></g>
    </svg>
    <svg class="ad__dots ad__dots--mid" width="110" height="140" viewBox="0 0 110 140">
      <g fill="var(--dot)">
        <circle cx="4" cy="6" r="2.5"/><circle cx="36" cy="6" r="2.5"/><circle cx="70" cy="6" r="2.5"/>
        <circle cx="4" cy="38" r="2.5"/><circle cx="36" cy="38" r="2.5"/><circle cx="70" cy="38" r="2.5"/>
        <circle cx="4" cy="70" r="2.5"/><circle cx="36" cy="70" r="2.5"/><circle cx="70" cy="70" r="2.5"/><circle cx="103" cy="70" r="2.5"/>
        <circle cx="4" cy="102" r="2.5"/><circle cx="36" cy="102" r="2.5"/><circle cx="70" cy="102" r="2.5"/><circle cx="103" cy="102" r="2.5"/>
        <circle cx="4" cy="134" r="2.5"/><circle cx="36" cy="134" r="2.5"/><circle cx="70" cy="134" r="2.5"/><circle cx="103" cy="134" r="2.5"/>
      </g>
    </svg>

    <h1 class="title">BRIGHT PARENT</h1>
    <div class="title__script">Reboot</div>

    <svg class="lead-arrows" width="66" height="26" viewBox="0 0 66 26">
      <g fill="none" stroke="var(--grey-chevron)" stroke-width="5">
        <polyline points="4,3 14,13 4,23"/><polyline points="20,3 30,13 20,23"/>
        <polyline points="36,3 46,13 36,23"/><polyline points="52,3 62,13 52,23"/>
      </g>
    </svg>
    <div class="start-label">STARTING</div>
    <div class="start-month">SEPTEMBER</div>
    <div class="date-box">
      <div class="date-box__day">23</div>
      <div class="date-box__year">2024</div>
    </div>

    <svg class="back-chevrons" width="130" height="60" viewBox="0 0 130 60">
      <g fill="var(--grey-chevron)">
        <polygon points="26,0 44,0 20,30 44,60 26,60 2,30"/>
        <polygon points="66,0 84,0 60,30 84,60 66,60 42,30"/>
        <polygon points="106,0 124,0 100,30 124,60 106,60 82,30"/>
      </g>
    </svg>

    <div class="brand">
      <div class="brand__name">PulseForge</div>
      <div class="brand__tag">PERSONAL GROUP TRAINING</div>
    </div>

    <div class="follow">
      <span>Follow us on</span>
      <span class="follow__dot"></span>
    </div>
  </section>
</body>
</html>
```